Title: “The Lantern Path, Rebuilding The Spirit of Harbors, A Sailor’s Journal”

Cover design for ebook and printable book. Looking for this specific designer

```html
<!DOCTYPE html>
<html lang="en">
<head>
<meta charset="UTF-8">
<title>The Lantern Path — Book Cover</title>
<link href="https://fonts.googleapis.com/css2?family=Noto+Serif:wght@400&family=Poppins:wght@400;700&display=swap" rel="stylesheet">
<style>
  :root {
    --page-bg: #e6e8ea;
    --cover-top: #f7f9fa;
    --cover-bottom: #eef2f4;
    --ink-blue: #1a6896;
    --ink-navy: #1b5780;
    --art-light: #dbeaf3;
    --art-mid: #a9cfe6;
    --spine-shade: rgba(0, 0, 0, 0.06);
  }
  * { margin: 0; padding: 0; box-sizing: border-box; }
  html, body {
    width: 1128px;
    height: 1200px;
    overflow: hidden;
    background: var(--page-bg);
  }
  .book-cover {
    position: absolute;
    left: 166px;
    top: 0;
    width: 795px;
    height: 1200px;
    background: linear-gradient(180deg, var(--cover-top), var(--cover-bottom));
    overflow: hidden;
  }
  .book-cover::before {
    content: "";
    position: absolute;
    left: 0; top: 0; bottom: 0;
    width: 18px;
    background: linear-gradient(90deg, var(--spine-shade), transparent);
  }
  .cover-art {
    position: absolute;
    left: 189px;
    top: 725px;
    width: 398px;
    height: 347px;
    border-radius: 50%;
    background: radial-gradient(circle at 50% 50%, var(--art-mid) 0%, var(--art-light) 55%, transparent 72%);
  }
  .cover-text {
    position: absolute;
    inset: 0;
  }
  .title {
    font-family: "Noto Serif", serif;
    font-size: 143px;
    fill: var(--ink-blue);
  }
  .subtitle-lead {
    font-family: "Poppins", sans-serif;
    font-size: 48px;
    fill: var(--ink-navy);
  }
  .subtitle-line {
    font-family: "Poppins", sans-serif;
    font-size: 28px;
    fill: var(--ink-navy);
  }
  .author {
    font-family: "Poppins", sans-serif;
    font-weight: 700;
    font-size: 28px;
    letter-spacing: 0.5px;
    fill: var(--ink-navy);
  }
</style>
</head>
<body>
  <main class="book-cover">
    <div class="cover-art" role="img" aria-label="Illustration of a light blue ship's lantern with its handle curving upward"></div>
    <svg class="cover-text" width="795" height="1200" viewBox="0 0 795 1200" xmlns="http://www.w3.org/2000/svg">
      <text class="title" x="739" y="170" text-anchor="end">The</text>
      <text class="title" x="739" y="275" text-anchor="end">Lantern</text>
      <text class="title" x="739" y="379" text-anchor="end">Path</text>
      <text class="subtitle-lead" x="743" y="546" text-anchor="end">Rebuilding</text>
      <text class="subtitle-line" x="743" y="588" text-anchor="end">The Spirit of Harbors</text>
      <text class="subtitle-line" x="743" y="632" text-anchor="end">A Sailor’s Journal</text>
      <text class="author" x="396" y="1164" text-anchor="middle">MARTIN COLE, M.D.</text>
    </svg>
  </main>
</body>
</html>
```